Submittal Letter - Letterhead

want something that matches our colors that looks professional for a design build engineering fan. Feel Free to incorporate Engineering, Procurement, Construction and Maintenance as a tagline type heading if it makes sense.

```html
<!DOCTYPE html>
<html lang="en">
<head>
<meta charset="utf-8">
<title>Submittal Letter – Letterhead</title>
<link href="https://fonts.googleapis.com/css2?family=Barlow:wght@400;500;600&family=Montserrat:wght@600&display=swap" rel="stylesheet">
<style>
  :root {
    --red: #d62a36;
    --black: #0c0c0c;
    --ink: #2b2b2b;
    --paper: #ffffff;
    --backdrop: #e3e3e3;
    --sig-fill: #e6e6e6;
  }
  * { margin: 0; padding: 0; box-sizing: border-box; }
  html, body {
    width: 1200px; height: 1200px; overflow: hidden;
    background: var(--backdrop);
  }
  .letterhead {
    position: absolute; left: 176px; top: 0;
    width: 848px; height: 1200px;
    background: var(--paper);
    font-family: "Barlow", sans-serif;
    color: var(--ink);
  }
  .top-rule {
    position: absolute; left: 0; top: 0; width: 100%; height: 14px;
    background: var(--black);
  }
  .top-rule .accent {
    position: absolute; left: 58px; top: 0; width: 174px; height: 100%;
    background: var(--red);
  }
  .brand {
    position: absolute; left: 60px; top: 94px;
    display: flex; align-items: center; gap: 10px;
  }
  .brand .dot {
    width: 34px; height: 34px; border-radius: 50%; background: var(--red);
  }
  .brand .name {
    font-weight: 600; font-size: 26px; color: var(--black); letter-spacing: .3px;
  }
  .contact {
    position: absolute; right: 80px; top: 70px;
    text-align: right; font-size: 13.4px; line-height: 18px;
  }
  .contact .row { display: flex; justify-content: flex-end; align-items: center; gap: 3px; }
  .contact .gap { margin-top: 3px; }
  .contact svg { width: 10px; height: 10px; }
  .recipient {
    position: absolute; left: 79px; top: 270px;
    font-size: 14.6px; line-height: 19px;
  }
  .salutation {
    position: absolute; left: 79px; top: 401px; font-size: 14.6px;
  }
  .body {
    position: absolute; left: 79px; top: 450px; width: 689px;
    font-size: 14.7px; line-height: 25.6px; text-align: justify;
  }
  .signer {
    position: absolute; left: 75px; top: 930px;
    font-family: "Montserrat", sans-serif; font-weight: 600;
    font-size: 13.5px; letter-spacing: 2.6px; color: var(--black);
  }
  .signature {
    position: absolute; left: 75px; top: 950px; width: 250px; height: 72px;
    background: var(--sig-fill); border-radius: 4px;
  }
  .footer-band {
    position: absolute; left: 0; top: 1142px; width: 100%; height: 27px;
    background: var(--black);
  }
  .footer-band .tagline-strip {
    position: absolute; left: 0; top: 0; width: 665px; height: 100%;
    background: var(--red); color: #fff;
    font-size: 12.6px; line-height: 27px; padding-left: 77px; letter-spacing: .3px;
  }
  .footer-band .sep { font-weight: 600; margin: 0 2px; }
  .footer-mark {
    position: absolute; left: 690px; top: 0; height: 27px;
    display: flex; align-items: center; gap: 6px;
    color: #fff; font-size: 12.6px; font-weight: 600;
  }
  .footer-mark .dot { width: 12px; height: 12px; border-radius: 50%; background: var(--red); }
</style>
</head>
<body>
<main class="letterhead">
  <div class="top-rule"><div class="accent"></div></div>

  <div class="brand">
    <span class="dot"></span>
    <span class="name">Harlow Kent</span>
  </div>

  <address class="contact" style="font-style:normal">
    <div class="row">4170 Meridian Avenue</div>
    <div class="row">Linden Park, CA 90655</div>
    <div class="row gap">(800) 555-0142
      <svg viewBox="0 0 10 10"><path d="M2 1l2 .3.5 2-1 .8a5 5 0 0 0 2.4 2.4l.8-1 2 .5.3 2C8 9 7 9.3 6 9 3.5 8 2 6.5 1 4 .7 3 1 2 2 1z" fill="var(--red)"/></svg>
    </div>
    <div class="row gap">www.hkinc.com
      <svg viewBox="0 0 10 10"><circle cx="5" cy="5" r="4.2" fill="none" stroke="var(--red)" stroke-width="1"/><path d="M1 5h8M5 .8c-2 2.5-2 5.9 0 8.4M5 .8c2 2.5 2 5.9 0 8.4" fill="none" stroke="var(--red)" stroke-width=".8"/></svg>
    </div>
  </address>

  <div class="recipient">
    Ms. Laura Whitcombe<br>
    Senior Contract Administrator<br>
    Coastal Valley Transit Authority (CVTA)<br>
    250 North Harbor Street<br>
    Westfield, California 92800
  </div>

  <p class="salutation">Dear :</p>

  <div class="body">
    <p>Harlow Kent, Inc. (HKI) is pleased to submit our response to Request for Qualifications (RFQ) No. 4-2448 issued by the Coastal Valley Transit Authority (CVTA) for the Design-Build of the Hydrogen Fueling Station and Facility Modifications at Elm Grove Bus Base. We appreciate the opportunity to showcase our expertise and are eager to contribute to this important project in support of CVTA’s commitment to sustainable transportation solutions.</p>
    <p>As a corporation organized under the laws of California and authorized to conduct business within the state, we have thoroughly reviewed the RFQ. Enclosed in the forms section are our completed documents, including Form A - Letter of Transmittal and Certification, Form B - Contact Information, and Form C - Addenda Acknowledgement. We have also included a declaration regarding any actual or potential conflicts of interest related to this RFQ. Daniel Price serves as the Owner and General Manager of HKI, and he is the primary contact for this submission. Additional main points of contact include Mark Ellison, Director of Engineering (email: mellison@hkinc.com, phone: (714) 555-0187), and Paul Grant, CFO (email: pgrant@hkinc.com, phone: (714) 555-0163).</p>
    <p>HKI agrees to keep our submittal, including proposed fees, open for one hundred eighty (180) days. We understand that our submission constitutes a binding offer to provide the services outlined in the RFQ, and we acknowledge that CVTA is not obligated to accept any submission. All costs incurred in the preparation of this submittal will be borne solely by HKI.</p>
  </div>

  <p class="signer">JONATHAN DOE</p>
  <div class="signature" role="img" aria-label="Handwritten signature of Jonathan Doe"></div>

  <footer class="footer-band">
    <div class="tagline-strip">ENGINEERING <span class="sep">|</span> PROCUREMENT <span class="sep">|</span> CONSTRUCTION <span class="sep">|</span> MAINTENANCE</div>
    <div class="footer-mark"><span class="dot"></span>Harlow Kent</div>
  </footer>
</main>
</body>
</html>
```